Ferris + Oakdale Architecture Ltd Stationary rebrand Lead designer to create a fresh clean modern...

We have recieved a great new logo design and now we are after a consistant fresh and modern stationary to match the new design. Business card design, Letter Head design, presentatnion folders and other stationery within the package. I have also added some of our existing layouts for presentation we would like updating with the new look, We would like a clean modern fresh design that looks visually pleasing on the page. we cant wait to see what you come up with!!!!

Target Market(s)

young professionals and middle age clients

Industry/Entity Type

Architect

Contact Information for Business Card

i have uploarded our orginal business card that has all the details attached.

Font styles to use
Sans Serif

Colors
000000
ffffff
d3d3d3

Requirements
Must have
• Logo and our contact information
Nice to have
• white sape around the card to give a clean look.

```html
<!DOCTYPE html>
<html lang="en">
<head>
<meta charset="utf-8">
<title>Ferris + Oakdale Architecture – Stationery</title>
<link href="https://fonts.googleapis.com/css2?family=Lato:wght@400;700&family=Montserrat:wght@500;600&display=swap" rel="stylesheet">
<style>
:root{
  --black:#000000;
  --ink:#231f20;
  --white:#ffffff;
  --grey:#d3d3d3;
  --bg:#efefef;
  --text:#555555;
  --accent:#d62828;
}
*{box-sizing:border-box;margin:0;padding:0}
html,body{width:1057px;height:1200px;overflow:hidden;background:var(--bg)}
body{position:relative;font-family:"Lato",sans-serif;color:var(--text);-webkit-font-smoothing:antialiased;-moz-osx-font-smoothing:grayscale}
/* keep small type in neutral greys (no coloured sub-pixel fringes) */
.sheet > *:not(.key):not(.render),.folder > *,.key > li:not(.last){filter:grayscale(1)}
.sheet{position:absolute;background:var(--white)}
.head{font-family:"Montserrat",sans-serif;font-weight:600;letter-spacing:.18em;color:var(--ink);text-transform:uppercase}

/* brand mark: plain square + name in one weight */
.brand{display:flex;flex-direction:column;align-items:center;font-family:"Montserrat",sans-serif;font-weight:500;text-transform:uppercase;color:var(--black);line-height:1.25;text-align:center}
.brand .sq{border:2px solid currentColor;margin-bottom:3px}
.brand .nm{letter-spacing:.08em}
.brand .sub{letter-spacing:.45em}
.brand.light{color:var(--white)}

/* letterhead */
.letterhead{left:166px;top:37px;width:301px;height:425px;font-size:5px}
.letterhead .brand{position:absolute;left:18px;top:34px;align-items:center}
.letterhead p{position:absolute;left:19px;width:262px;line-height:8px;text-align:justify}
.lh-sign{position:absolute;left:19px;top:300px;line-height:6px}
.lh-sign .name{font-size:7.5px;line-height:8px;color:#333}
.lh-sig{position:absolute;left:19px;top:316px;width:54px;height:22px;background:#f2f2f2}
.lh-foot{position:absolute;top:398px;font-size:4.6px;line-height:6px;color:#333}

/* business cards */
.card-front{left:458px;top:166px;width:149px;height:85px;background:var(--black);display:flex;align-items:center;justify-content:center}
.card-back{left:458px;top:264px;width:149px;height:84px;font-size:3.2px;line-height:4px;color:#333}
.card-back .who{position:absolute;left:12px;top:9px;font-size:5px;line-height:6px;letter-spacing:.12em;color:var(--black)}
.card-back .who span{display:block;font-size:3px;line-height:4px;margin-top:0;letter-spacing:.15em}
.card-back .det{position:absolute;left:11px;top:34px}
.card-back .det div{margin-bottom:3px}
.card-back .brand{position:absolute;right:10px;bottom:12px}

/* folder */
.folder{position:absolute;left:173px;top:493px;width:264px;height:356px}
.folder-title{position:absolute;left:42px;top:18px;width:222px;text-align:center;color:var(--white)}
.folder-title .head{color:var(--white);font-size:5.6px;font-weight:500}
.folder-title .loc{font-family:"Montserrat",sans-serif;font-size:3.6px;letter-spacing:.2em;line-height:5px;margin-top:4px;text-transform:uppercase}
.folder .brand{position:absolute;left:42px;width:222px;top:56px}

/* drawing set cover */
.cover{left:437px;top:493px;width:221px;height:305px}
.cover .ttl{position:absolute;top:23px;width:100%;text-align:center;font-size:5.6px;font-weight:500}
.cover .loc{position:absolute;top:32px;width:100%;text-align:center;font-family:"Montserrat",sans-serif;font-size:3.8px;letter-spacing:.25em;line-height:5px;color:var(--ink);text-transform:uppercase}
.cover .brand{position:absolute;top:56px;width:100%}
.key{position:absolute;left:20px;top:102px;font-size:3.4px;line-height:5.1px;color:#333;list-style:none}
.key .hd{font-size:4.2px;margin-bottom:5px;color:var(--ink)}
.key li.last{color:var(--accent)}
.render{position:absolute;background:linear-gradient(180deg,#b9cde0 0%,#d4d8dc 55%,#9a8f84 75%,#a7a7a7 100%)}

/* specification */
.spec{left:677px;top:495px;width:221px;height:305px;color:#333}
.spec .brand{position:absolute;top:23px;width:100%}
.spec .s-head{position:absolute;left:56px;top:101px;font-size:6.6px}
.spec .s-sub{position:absolute;left:56px;top:113px;font-size:3.2px;line-height:4px;width:100px}
.spec .s-line{position:absolute;left:56px;font-family:"Montserrat",sans-serif;font-size:4.4px;letter-spacing:.2em;color:#333}
.spec .s-client{position:absolute;left:56px;top:169px;font-size:7px;line-height:8px}
.spec .s-client .addr{font-weight:500;font-size:4.4px;line-height:5px;margin-top:1px}
.spec .s-meta{position:absolute;left:159px;top:259px;font-size:4px;line-height:4.8px}
.spec .s-foot{position:absolute;top:285px;font-size:3.8px;font-style:italic;line-height:4.8px}

/* envelope */
.env-front{left:184px;top:893px;width:195px;height:98px}
.env-back{left:184px;top:996px;width:195px;height:99px;font-size:2.8px;line-height:3.6px;color:#333}
.env-back .band{position:absolute;left:0;top:0;width:100%;height:2px;background:var(--black)}
.env-back .brand{position:absolute;left:17px;top:20px}
.env-back .det{position:absolute;left:18px;top:52px}
.env-back .det div{margin-bottom:2px}
.env-window{position:absolute;left:116px;top:50px;width:65px;height:30px;border-radius:7px;background:linear-gradient(120deg,#e2e2e2 0%,#cfcfcf 50%,#dcdcdc 100%);border:1px solid #c4c4c4}

/* presentation sheets */
.pres{top:827px;width:222px;height:305px}
.pres .brand{position:absolute;top:22px;width:100%}
.pres .p-title{position:absolute;top:268px;width:100%;text-align:center;font-size:6.4px;line-height:8px}
.pres .p-note{position:absolute;top:288px;width:100%;text-align:center;font-size:2.9px;line-height:3.8px;color:#333}
.persp{left:431px}
.plans{left:673px}
.plan-area{position:absolute;left:13px;top:80px;width:186px;height:125px;background:linear-gradient(180deg,#ffffff 0%,#f1f1f1 100%)}
.plans .fp{position:absolute;left:30px;top:212px;color:var(--ink)}
.plans .fp .head{font-size:6.6px}
.plans .fp .data{font-size:3.2px;line-height:4.5px;margin-top:7px;color:#333}
</style>
</head>
<body>

<!-- Letterhead -->
<section class="sheet letterhead">
  <div class="brand" style="font-size:4.2px">
    <span class="sq" style="width:22px;height:22px"></span>
    <span class="nm">Ferris + Oakdale</span>
    <span class="sub">Architecture</span>
  </div>
  <p style="top:98px">Date : 14.06.2019</p>
  <p style="top:129px">Dear, Mr____________</p>
  <p style="top:150px">Lorem Ipsum is simply dummy text of the printing and typesetting industry. Lorem Ipsum has been the industry's standard dummy text ever since the1500s,when an unknown printer took a galley of type and scrambled it to make a type specimen book. It has survived not only five centuries, but also the leap into electronic typesetting, remaining essentially unchanged.</p>
  <p style="top:190px">Lorem Ipsum is simply dummy text of the printing and typesetting industry. Lorem Ipsum has been the industry's standard dummy text ever since the1500s.</p>
  <p style="top:213px">Lorem Ipsum is simply dummy text of the printing and typesetting industry.</p>
  <div class="lh-sign"><div class="name">Your Name</div><div>Designation</div></div>
  <div class="lh-sig" role="img" aria-label="Handwritten signature"></div>
  <div class="lh-foot" style="left:20px">A : 18 Harlow Street Ashford 7710<br>P : PO Box 4410 Ashford 7742</div>
  <div class="lh-foot" style="left:139px">T : 03 555 0148<br>M : 0270 555 219</div>
  <div class="lh-foot" style="left:215px;text-align:right">E : daniel@foarchitecture.co.nz<br>W : www.foarchitecture.co.nz</div>
</section>

<!-- Business card front -->
<section class="sheet card-front">
  <div class="brand light" style="font-size:4.4px">
    <span class="sq" style="width:22px;height:22px"></span>
    <span class="nm">Ferris + Oakdale</span>
    <span class="sub">Architecture</span>
  </div>
</section>

<!-- Business card back -->
<section class="sheet card-back">
  <div class="who head">Daniel Ferris<span>Director</span></div>
  <div class="det">
    <div>A : 18 Harlow Street<br>&nbsp;&nbsp;&nbsp;&nbsp;&nbsp;Ashford 7710<br>P : PO Box 4410<br>&nbsp;&nbsp;&nbsp;&nbsp;&nbsp;Ashford 7742</div>
    <div>T : 03 555 0148<br>M : 0270 555 219</div>
    <div>E : daniel@foarchitecture.co.nz<br>W : www.foarchitecture.co.nz</div>
  </div>
  <div class="brand" style="font-size:3px">
    <span class="sq" style="width:14px;height:14px;border-width:1.5px"></span>
    <span class="nm">Ferris + Oakdale</span>
    <span class="sub">Architecture</span>
  </div>
</section>

<!-- Presentation folder -->
<section class="folder">
  <svg width="264" height="356" viewBox="0 0 264 356" aria-hidden="true">
    <polygon points="0,28 42,0 42,305 0,285" fill="var(--ink)"/>
    <rect x="42" y="0" width="222" height="305" fill="var(--ink)"/>
    <polygon points="42,305 264,305 207,356 42,356" fill="var(--ink)"/>
  </svg>
  <div class="folder-title">
    <div class="head">Harwood House Concept</div>
    <div class="loc">Kestrel Street<br>Fairhaven<br>2019</div>
  </div>
  <div class="brand light" style="font-size:4.2px">
    <span class="sq" style="width:22px;height:22px"></span>
    <span class="nm">Ferris + Oakdale</span>
    <span class="sub">Architecture</span>
  </div>
</section>

<!-- Drawing set cover -->
<section class="sheet cover">
  <div class="ttl head">Marlow Commercial Development</div>
  <div class="loc">63 - 67 Avery Street<br>Brookvale<br>2018</div>
  <div class="brand" style="font-size:4.2px">
    <span class="sq" style="width:22px;height:22px"></span>
    <span class="nm">Ferris + Oakdale</span>
    <span class="sub">Architecture</span>
  </div>
  <ul class="key">
    <li class="hd">KEY TO DRAWINGS</li>
    <li>01&nbsp; Existing Site Plan</li><li>02&nbsp; Proposed Site Plan</li><li>03&nbsp; Ground Floor Plan</li>
    <li>04&nbsp; First Floor Plan</li><li>05&nbsp; Elevations</li><li>06&nbsp; Elevations</li>
    <li>07&nbsp; Roof Plan</li><li>08&nbsp; Sections A &amp; B</li><li>09&nbsp; Sections C &amp; D</li>
    <li>10&nbsp; Door Schedule</li><li>11&nbsp; Window Schedule</li><li>12&nbsp; Window Schedule</li>
    <li>13&nbsp; Internal Joinery</li><li>14&nbsp; Floor Covering Splan</li><li>15&nbsp; Wall Linings Plan</li>
    <li>16&nbsp; Reflected Ceiling Plan</li><li>17&nbsp; Glass Canopies</li><li>18&nbsp; Glass Canopies</li>
    <li>19&nbsp; Glass Canopies</li><li>20&nbsp; Glass Canopies</li><li>21&nbsp; Weathering Details</li>
    <li>22&nbsp; Weathering Details</li><li>23&nbsp; Weathering Details</li><li>24&nbsp; Weathering Details</li>
    <li>25&nbsp; Weathering Details</li><li>26&nbsp; Weathering Details</li><li>27&nbsp; Weathering Details</li>
    <li>28&nbsp; Weathering Details</li><li>29&nbsp; Weathering Details</li><li>30&nbsp; Weathering Details</li>
    <li class="last">31&nbsp; SECTION E</li>
  </ul>
  <div class="render" style="left:80px;top:105px;width:121px;height:80px" role="img" aria-label="Rendered view of the two-storey commercial building with timber-clad corner"></div>
  <div class="render" style="left:80px;top:200px;width:121px;height:71px" role="img" aria-label="Street-level render of the commercial development frontage"></div>
</section>

<!-- Specification cover -->
<section class="sheet spec">
  <div class="brand" style="font-size:4.2px">
    <span class="sq" style="width:22px;height:22px"></span>
    <span class="nm">Ferris + Oakdale</span>
    <span class="sub">Architecture</span>
  </div>
  <div class="s-head head">Specification</div>
  <div class="s-sub">of work to be done and materials to be used in carrying out the works shown on the accompanying drawings</div>
  <div class="s-line" style="top:141px">New Dwelling</div>
  <div class="s-line" style="top:153px">for</div>
  <div class="s-client head">A &amp; N Reeve<div class="addr">64 Kinloch Drive<br>Lakefield</div></div>
  <div class="s-meta">Project No. 19020<br>Date: MAY 2019<br>ISSUE: Building Consent</div>
  <div class="s-foot" style="left:18px">FERRIS + OAKDALE<br>ARCHITECTURE LTD</div>
  <div class="s-foot" style="left:161px">CONSENT ISSUE Page 1</div>
</section>

<!-- Envelope front -->
<section class="sheet env-front">
  <svg width="195" height="98" viewBox="0 0 195 98" aria-hidden="true">
    <path d="M0,0 H195 L191,28 Q190,32 186,32 H9 Q5,32 4,28 Z" fill="var(--black)"/>
  </svg>
</section>

<!-- Envelope back -->
<section class="sheet env-back">
  <div class="band"></div>
  <div class="brand" style="font-size:2.8px">
    <span class="sq" style="width:13px;height:13px;border-width:1.5px"></span>
    <span class="nm">Ferris + Oakdale</span>
    <span class="sub">Architecture</span>
  </div>
  <div class="det">
    <div>A : 18 Harlow Street<br>&nbsp;&nbsp;&nbsp;&nbsp;&nbsp;Ashford 7710<br>P : PO Box 4410<br>&nbsp;&nbsp;&nbsp;&nbsp;&nbsp;Ashford 7742</div>
    <div>T : 03 555 0148<br>M : 0270 555 219</div>
    <div>E : daniel@foarchitecture.co.nz<br>W : www.foarchitecture.co.nz</div>
  </div>
  <div class="env-window"></div>
</section>

<!-- Presentation: perspectives -->
<section class="sheet pres persp">
  <div class="brand" style="font-size:4.2px">
    <span class="sq" style="width:22px;height:22px"></span>
    <span class="nm">Ferris + Oakdale</span>
    <span class="sub">Architecture</span>
  </div>
  <div class="render" style="left:39px;top:64px;width:147px;height:86px;background:linear-gradient(180deg,#5a7593 0%,#8fa6bd 45%,#3f3f3f 62%,#4c5b2d 75%,#55672f 100%)" role="img" aria-label="Perspective render of the house with dark cladding and lawn"></div>
  <div class="render" style="left:38px;top:160px;width:147px;height:86px;background:linear-gradient(180deg,#6b85a1 0%,#9fb2c4 45%,#353535 62%,#4a5a2c 75%,#56682f 100%)" role="img" aria-label="Rear perspective render of the house across the lawn"></div>
  <div class="p-title head">Harwood House Concept<br>Perspectives</div>
  <div class="p-note">The design and drawings shown on this set of documents are not to be reproduced<br>without the written authority of FERRIS + OAKDALE ARCHITECTURE LTD and their copyright .</div>
</section>

<!-- Presentation: floor plans -->
<section class="sheet pres plans">
  <div class="brand" style="font-size:4.2px">
    <span class="sq" style="width:22px;height:22px"></span>
    <span class="nm">Ferris + Oakdale</span>
    <span class="sub">Architecture</span>
  </div>
  <div class="plan-area" role="img" aria-label="Proposed floor plan drawing on the site boundary"></div>
  <div class="fp">
    <div class="head">Proposed Floor Plan</div>
    <div class="data">SCALE 1:100 @ &nbsp;&nbsp;&nbsp;&nbsp;&nbsp;&nbsp;&nbsp;&nbsp;A2<br><b>FLOOR AREAS:</b><br>HOUSE FLOOR AREA: &nbsp;&nbsp;278.0m2</div>
  </div>
  <div class="p-title head">Harwood House Concept<br>Floor Plans</div>
  <div class="p-note">The design and drawings shown on this set of documents are not to be reproduced without the written authority<br>of FERRIS + OAKDALE ARCHITECTURE LTD and their copyright</div>
</section>

</body>
</html>
```